Harlow Ironworks Business Card

We need a business card design for a new small metal fabrication business in rural NSW, Australia.

The business (Harlow Ironworks) is owner operated by a man with the initials KB - much of the branding comes from this name.

Harlow Ironworks designs, engineers, repairs and manufactures a range of custom, quality metal works including vehicle trays, agricultural machinery impliments, trailers, wood splitters, fire pits, furniture etc.

The brand position focuses on custom work of the highest quality.

Business card design should show quality, attention to detail and stand out among a mass of business cards.

Logos are in the files

The grey color may be changed on the logo if required to stand out more.

There is an image attached of a simple card that is liked because it is clean, clear, simple, masculine and effective. It says 'quality'. As most of the work we do is custom it would be good to have the business card speak to this.

Target Market(s)

Rural and regional based Australians. Primarily adult male 25-60 yrs. Primary production / rural / travelling lifestyle.

Industry/Entity Type

Metal Fabrication

Contact Information for Business Card

The words 'custom quality fabrications' would be great somewhere perhaps on the backside (not on the information side)
Name
title
Phone: 0418 539 746 and (02) 6193 4827
email: info@harlowiw.com.au
www.harlowiw.com.au

address (2 lines)

Requirements
Nice to have
• Background colour should be very navy blue or black.
Should not have
• NO orange and blue combinations.
• Navy is OK

```html
<!DOCTYPE html>
<html lang="en">
<head>
<meta charset="utf-8">
<title>Harlow Ironworks Business Card</title>
<link rel="stylesheet" href="https://fonts.googleapis.com/css2?family=Montserrat:wght@300;400;600;700&display=swap">
<style>
  :root {
    --page: #ececea;
    --card: #161616;
    --ink: #ffffff;
    --muted: #8a8a8a;
    --soft: #6c6c6c;
    --rule: #5a5a5a;
    --accent: #5bbd3a;
    --steel: #b5b5b5;
  }
  * { margin: 0; padding: 0; box-sizing: border-box; }
  html, body { width: 960px; height: 1200px; overflow: hidden; }
  body {
    background: var(--page);
    font-family: "Montserrat", sans-serif;
    display: flex;
    flex-direction: column;
    align-items: center;
    justify-content: center;
    gap: 60px;
  }
  .card {
    position: relative;
    width: 840px;
    height: 480px;
    background: var(--card);
    box-shadow: 0 10px 30px rgba(0,0,0,.25);
    overflow: hidden;
  }

  /* Front: contact side */
  .front__brand {
    position: absolute;
    left: 60px; top: 150px;
    width: 300px;
    display: flex;
    align-items: center;
    gap: 16px;
  }
  .brand-square {
    width: 34px; height: 34px;
    background: var(--steel);
    flex: none;
  }
  .brand-name {
    font-weight: 700;
    font-size: 27px;
    line-height: 1.15;
    letter-spacing: 1px;
    text-transform: uppercase;
    color: var(--steel);
  }
  .front__divider {
    position: absolute;
    left: 400px; top: 80px;
    width: 1px; height: 230px;
    background: var(--rule);
  }
  .front__details {
    position: absolute;
    left: 445px; top: 70px;
  }
  .person-name {
    font-weight: 700;
    font-size: 34px;
    color: var(--ink);
    letter-spacing: .5px;
  }
  .person-name .surname { color: var(--accent); }
  .person-title {
    font-weight: 400;
    font-size: 25px;
    color: var(--muted);
    margin-top: 2px;
  }
  .contact-list {
    list-style: none;
    margin-top: 22px;
  }
  .contact-list li {
    display: flex;
    align-items: center;
    gap: 14px;
    font-size: 19px;
    font-weight: 300;
    color: var(--muted);
    height: 36px;
  }
  .contact-icon { width: 22px; height: 22px; flex: none; }
  .front__address {
    position: absolute;
    left: 0; right: 0; bottom: 60px;
    text-align: center;
    font-size: 19px;
    font-weight: 300;
    color: var(--soft);
  }

  /* Back: brand side */
  .back__brand {
    position: absolute;
    left: 0; right: 0; top: 120px;
    display: flex;
    justify-content: center;
    align-items: center;
    gap: 18px;
  }
  .back__brand .brand-square { background: var(--accent); width: 40px; height: 40px; }
  .back__brand .brand-name { font-size: 36px; color: var(--steel); }
  .back__rule {
    position: absolute;
    left: 60px; right: 60px; top: 290px;
    height: 1px;
    background: var(--rule);
  }
  .tagline {
    position: absolute;
    left: 0; right: 0; top: 340px;
    text-align: center;
    font-size: 22px;
    font-weight: 400;
    letter-spacing: .5px;
    color: var(--soft);
  }
</style>
</head>
<body>

  <section class="card card--front" aria-label="Business card front">
    <div class="front__brand">
      <span class="brand-square"></span>
      <span class="brand-name">Harlow Ironworks</span>
    </div>
    <div class="front__divider"></div>
    <div class="front__details">
      <h1 class="person-name">SAM <span class="surname">REYES</span></h1>
      <p class="person-title">Manager</p>
      <ul class="contact-list">
        <li>
          <svg class="contact-icon" viewBox="0 0 22 22"><circle cx="11" cy="11" r="11" fill="#8a8a8a"/><path d="M7 8c1-2 2-2 3-1l-1 2c1 2 2 3 4 4l2-1c1 1 1 2-1 3-4 0-8-4-7-7z" fill="#161616"/></svg>
          0418 539 746
        </li>
        <li>
          <svg class="contact-icon" viewBox="0 0 22 22"><circle cx="11" cy="11" r="11" fill="#8a8a8a"/><rect x="6" y="9" width="10" height="6" rx="1" fill="#161616"/><rect x="7" y="6.5" width="8" height="2" rx="1" fill="#161616"/></svg>
          (02) 6193 4827
        </li>
        <li>
          <svg class="contact-icon" viewBox="0 0 22 22"><circle cx="11" cy="11" r="11" fill="#8a8a8a"/><rect x="5.5" y="7.5" width="11" height="7" fill="#161616"/><path d="M5.5 7.5l5.5 4 5.5-4" stroke="#8a8a8a" fill="none"/></svg>
          info@harlowiw.com.au
        </li>
        <li>
          <svg class="contact-icon" viewBox="0 0 22 22"><circle cx="11" cy="11" r="11" fill="#8a8a8a"/><circle cx="11" cy="11" r="5.5" fill="none" stroke="#161616" stroke-width="1.3"/><path d="M5.5 11h11M11 5.5c-3 3-3 8 0 11M11 5.5c3 3 3 8 0 11" stroke="#161616" fill="none"/></svg>
          www.harlowiw.com.au
        </li>
      </ul>
    </div>
    <p class="front__address">48 Quarry Road, Tumut NSW 2720</p>
  </section>

  <section class="card card--back" aria-label="Business card back">
    <div class="back__brand">
      <span class="brand-square"></span>
      <span class="brand-name">Harlow Ironworks</span>
    </div>
    <div class="back__rule"></div>
    <p class="tagline">Custom Quality Fabrications</p>
  </section>

</body>
</html>
```